Paveline Ridge

Im looking for something similar to (tarvexblacktop.example) web site. I really want it to pop!
services we offer:
- Seal Coating
- Crack Filling
- Striping
- Asphalt
- Concrete
- Signage
- Road Grinding
- Grading
- Hydro Blasting
- Recycled asphalt
- Dumpster Pads
- Pressure Washing
- Wheel blocks
- Bollard installation
- Commercial Curbing
- Job site clean up
- Sweeping
- Forestry Clean up
- ADA Compliant work
- Speed bump installation and removal
- Snow removal
- Custom stair sets (Commercial)
Target Market(s)
Parking lot maintenance, asphalt repairs, road grading
Industry/Entity Type
construction, parking lot maintenance

```html
<!DOCTYPE html>
<html lang="en">
<head>
<meta charset="utf-8">
<title>Paveline Ridge — Paving &amp; Parking Lot Maintenance</title>
<link rel="stylesheet" href="https://fonts.googleapis.com/css2?family=Archivo+Black&family=Arimo:wght@400;700&display=swap">
<style>
:root{
  --ink:#1d1e21;
  --ink-deep:#161719;
  --lime:#6df21c;
  --lime-text:#4fe01f;
  --white:#ffffff;
  --black:#0b0b0b;
}
*{box-sizing:border-box;margin:0;padding:0}
html,body{width:1200px;height:3566px;overflow:hidden}
body{background:var(--ink);color:var(--white);font-family:'Arimo',Arial,sans-serif;position:relative}
.abs{position:absolute}
.display{font-family:'Archivo Black','Arial Black',sans-serif;line-height:1.02}

/* header */
.brand{left:51px;top:60px;font-family:'Archivo Black','Arial Black',sans-serif;color:var(--lime-text);font-size:38px;line-height:1;width:260px}
.brand small{display:block;font-family:'Arimo',Arial,sans-serif;font-weight:700;font-size:16px;letter-spacing:9px;margin-top:8px}
.contact-item{font-size:19px;line-height:1.4;white-space:nowrap}
.contact-item b{display:block;color:var(--lime-text);font-weight:700;font-size:20px}
.menu{left:1084px;top:92px;width:73px}
.menu span{display:block;height:5px;background:var(--lime);margin-bottom:7px}

/* hero */
.hero{left:0;top:0;width:1200px;height:894px;background:linear-gradient(160deg,#222326 0%,#2a2b2e 45%,#4a4b4e 70%,#2b2c2f 100%)}
.hero-title{left:51px;top:300px;font-size:83px}
.hero-text{left:51px;top:498px;font-size:28px;line-height:1.28;width:600px}
.btn{left:51px;top:656px;width:424px;height:64px;background:var(--lime);border-radius:8px;color:var(--black);font-weight:700;font-size:28px;display:flex;align-items:center;justify-content:center}

/* services */
.section-title{font-size:72px}
.rule{height:5px;background:var(--lime)}
.service-list{font-size:22px;line-height:29.3px;list-style:none}
.tile{width:205px;height:207px;background:var(--lime);color:var(--black);font-weight:700;font-size:23px;text-align:center;display:flex;flex-direction:column;align-items:center;justify-content:flex-end;padding-bottom:28px;line-height:1.25}
.tile .icon{width:90px;height:70px;background:var(--black);border-radius:10px;margin-bottom:18px}

/* banner */
.banner{left:0;top:1672px;width:1200px;height:208px;background:var(--lime);color:var(--black);text-align:center}
.banner h2{font-family:'Archivo Black','Arial Black',sans-serif;font-size:58px;padding-top:40px;line-height:1}
.banner p{font-family:'Archivo Black','Arial Black',sans-serif;font-size:30px;margin-top:14px}
.banner p big{font-size:46px}

/* projects */
.project{width:254px;height:213px;border:3px solid var(--lime)}
.p-blue{background:linear-gradient(180deg,#5d7fc2 0%,#6b8dbb 40%,#2d3038 75%,#22252b 100%)}
.p-green{background:linear-gradient(180deg,#5a8bd0 0%,#2f5a2c 45%,#3b3e44 70%,#2a2d33 100%)}
.p-road{background:linear-gradient(180deg,#7a8a6a 0%,#6b6f67 45%,#3a3b3e 100%)}
.p-dark{background:linear-gradient(180deg,#3d3f45 0%,#1b1c1f 100%)}
.p-yellow{background:linear-gradient(180deg,#506a8a 0%,#c9a21a 50%,#2a2a2a 100%)}
.p-cones{background:linear-gradient(180deg,#8c9a7c 0%,#6f7478 50%,#5e5f62 100%)}

/* clients */
.clients{left:0;top:2736px;width:1200px;height:396px;background:var(--lime);color:var(--black)}
.client{font-family:'Arimo',Arial,sans-serif;font-weight:700;font-size:36px;color:var(--black);display:flex;align-items:center;gap:12px;white-space:nowrap}
.client i{display:inline-block;width:30px;height:30px;background:var(--black)}

/* footer */
.footer-rule{left:0;top:3176px;width:1200px;height:1px;background:#4a4b4e}
.footer-brand{left:44px;top:3262px;font-family:'Archivo Black','Arial Black',sans-serif;font-size:52px;line-height:1;color:var(--white)}
.footer-brand small{display:block;font-family:'Arimo',Arial,sans-serif;font-weight:700;font-size:24px;letter-spacing:13px;margin-top:12px}
.footer-links{left:44px;top:3394px;font-size:22px;letter-spacing:1px}
.social{width:47px;height:47px;border:3px solid var(--lime);top:3452px}
</style>
</head>
<body>

<div class="abs hero" role="img" aria-label="Dusk photograph of an empty winding asphalt road through open countryside"></div>

<header>
  <div class="abs brand">PAVELINE<small>RIDGE</small></div>
  <div class="abs contact-item" style="left:400px;top:84px"><b>OUR LOCATION</b>2200 HARLOW AVE.LA</div>
  <div class="abs contact-item" style="left:646px;top:82px"><b>EMAIL US</b>hello@paveline.example</div>
  <div class="abs contact-item" style="left:887px;top:82px"><b>CALL US</b>0 800 555 0142</div>
  <div class="abs menu"><span></span><span></span><span></span></div>
</header>

<section>
  <h1 class="abs display hero-title">In Business<br>Since 1990</h1>
  <p class="abs hero-text">Commercial, Industrial &amp; Paving. Asphalt &amp; Concrete Paving, Constuction, and Parking lot maintenance</p>
  <div class="abs btn">REQUEST FREE ESTIMATE</div>
</section>

<section>
  <h2 class="abs display section-title" style="left:65px;top:1028px">Our<br>Services</h2>
  <div class="abs rule" style="left:69px;top:1196px;width:332px"></div>
  <ul class="abs service-list" style="left:65px;top:1234px">
    <li>Seal Coating</li><li>Crack Filling</li><li>Striping</li><li>Asphalt</li><li>Concrete</li><li>Signage</li><li>Road Grinding</li><li>Grading</li><li>Recycled asphalt</li><li>Trucking</li>
  </ul>
  <ul class="abs service-list" style="left:256px;top:1240px">
    <li>Pressure Washing</li><li>Wheel blocks</li><li>Bollard installation</li><li>Commercial Curbing</li><li>Job site clean up</li><li>Forestry Clean up</li>
  </ul>

  <div class="abs tile" style="left:491px;top:1085px"><div class="icon" role="img" aria-label="Road roller icon"></div>Asphalt</div>
  <div class="abs tile" style="left:718px;top:1085px"><div class="icon" role="img" aria-label="Concrete mixer truck icon"></div>Concrete</div>
  <div class="abs tile" style="left:947px;top:1085px"><div class="icon" role="img" aria-label="Paving stones icon"></div>Pavment</div>
  <div class="abs tile" style="left:491px;top:1320px"><div class="icon" role="img" aria-label="Haul truck icon"></div>Trucking</div>
  <div class="abs tile" style="left:718px;top:1320px;padding-bottom:12px"><div class="icon" role="img" aria-label="Car at parking barrier icon"></div>Parking Lot<br>Maintenance</div>
  <div class="abs tile" style="left:947px;top:1320px"><div class="icon" role="img" aria-label="Street sweeper truck icon"></div>Clean ups</div>
</section>

<section class="abs banner">
  <h2>FREE ESTIMATE</h2>
  <p>CALL US ON <big>0800 555 800</big> FOR A FREE ESTIMATE</p>
</section>

<section>
  <h2 class="abs display section-title" style="left:53px;top:1966px">Recent Projects</h2>
  <div class="abs rule" style="left:60px;top:2058px;width:332px"></div>

  <div class="abs project p-blue" style="left:37px;top:2141px" role="img" aria-label="Crew raking fresh asphalt with a roller behind"></div>
  <div class="abs project p-road" style="left:331px;top:2141px" role="img" aria-label="Traffic cone on new asphalt with paving truck"></div>
  <div class="abs project p-green" style="left:624px;top:2141px" role="img" aria-label="Worker sealing a parking lot among pine trees"></div>
  <div class="abs project p-dark" style="left:913px;top:2141px" role="img" aria-label="Crew spreading asphalt beside a paver"></div>
  <div class="abs project p-green" style="left:37px;top:2399px" role="img" aria-label="Worker sealing a parking lot among pine trees"></div>
  <div class="abs project p-blue" style="left:331px;top:2399px" role="img" aria-label="Crew raking fresh asphalt with a roller behind"></div>
  <div class="abs project p-yellow" style="left:624px;top:2399px" role="img" aria-label="Yellow wheel loader at a work site"></div>
  <div class="abs project p-cones" style="left:913px;top:2399px" role="img" aria-label="Row of cones along a resurfaced road"></div>
</section>

<section class="abs clients">
  <h2 class="abs display" style="left:60px;top:47px;font-size:72px">Our Clients</h2>
  <div class="abs rule" style="left:78px;top:146px;width:332px;background:var(--black)"></div>
  <div class="abs client" style="left:125px;top:272px"><i></i>Stonevale</div>
  <div class="abs client" style="left:378px;top:272px">Brightmere</div>
  <div class="abs client" style="left:600px;top:272px">Orbitline</div>
  <div class="abs client" style="left:810px;top:272px">Kestrel Works</div>
</section>

<footer>
  <div class="abs footer-rule"></div>
  <div class="abs footer-brand">PAVELINE<small>RIDGE</small></div>
  <div class="abs contact-item" style="left:477px;top:3294px"><b>OUR LOCATION</b>2200 HARLOW AVE.LA</div>
  <div class="abs contact-item" style="left:724px;top:3292px"><b>EMAIL US</b>hello@paveline.example</div>
  <div class="abs contact-item" style="left:965px;top:3292px"><b>CALL US</b>0 800 555 0142</div>
  <nav class="abs footer-links">Home I Serices I About I Contact</nav>
  <div class="abs social" style="left:44px"></div>
  <div class="abs social" style="left:105px"></div>
  <div class="abs social" style="left:166px"></div>
  <div class="abs social" style="left:227px"></div>
  <div class="abs social" style="left:288px"></div>
  <div class="abs social" style="left:349px"></div>
</footer>

</body>
</html>
```